Landing Page für Anbieter von Finanzierungslösungen
Zielgruppe
Finanzierungslösungen für Gewerbe und Firmen. Fokus liegt auf der Finanzierung von Rechenzentren und deren Einrichtung.
Aufgabenstellung
Wir haben bereits Visitenkarten und Briefbögen designen lassen. Bitte daran anlehnen.

```html
<!DOCTYPE html>
<html lang="de">
<head>
<meta charset="utf-8">
<title>Veltrana – Finanzierung für Gewerbe &amp; Industrie</title>
<link href="https://fonts.googleapis.com/css2?family=Cormorant+Garamond:wght@500;600&family=Inter:wght@400;500;600&display=swap" rel="stylesheet">
<style>
:root{
  --blue:#0b6aa6;
  --blue-deep:#0a4f80;
  --green:#8cbf3f;
  --sky:#e3f3fc;
  --ink:#1b1f24;
  --muted:#4b5560;
  --navy:#0d3552;
  --white:#fff;
  --serif:"Cormorant Garamond",Georgia,serif;
  --sans:"Inter",Arial,sans-serif;
}
*{box-sizing:border-box;margin:0;padding:0}
html,body{width:1200px;height:3932px;overflow:hidden}
body{font-family:var(--sans);color:var(--ink);background:var(--white);position:relative}
section,header,footer{position:relative;width:1200px}
.abs{position:absolute}
.btn{display:inline-flex;align-items:center;gap:8px;font-size:12px;font-weight:500;color:#fff;text-decoration:none;justify-content:center}
.btn svg{width:12px;height:12px}

/* hero */
.hero{height:725px;overflow:hidden}
.hero-photo{position:absolute;inset:0;background:linear-gradient(115deg,#0d3f66 0%,#145f94 45%,#2d86c0 75%,#1a6aa3 100%)}
.nav{position:absolute;top:38px;left:76px;right:76px;height:42px;display:flex;align-items:center}
.brand{font-family:var(--sans);font-weight:600;font-size:34px;color:#fff;display:flex;align-items:center;gap:10px}
.brand i{width:14px;height:14px;border-radius:50%;background:var(--green)}
.nav-links{display:flex;gap:27px;margin-left:96px;font-size:13px;letter-spacing:.06em;color:#fff}
.nav-links a{color:#fff;text-decoration:none;padding-bottom:8px}
.nav-links .active{border-bottom:2px solid var(--green)}
.nav-cta{margin-left:auto;background:var(--green);color:#fff;font-size:13px;letter-spacing:.1em;padding:13px 20px}
.hero h1{position:absolute;left:76px;top:225px;font-family:var(--serif);font-weight:500;font-size:60px;line-height:1;color:#fff}
.hero p{position:absolute;left:76px;top:440px;width:580px;font-size:16.5px;line-height:1.45;color:#e8f1f8}
.hero .btn{position:absolute;top:552px;height:44px}
.btn-primary{background:var(--blue);left:76px;width:158px}
.btn-ghost{border:1.5px solid #fff;left:247px;width:151px}

/* stats */
.stats{height:135px;background:var(--green);display:flex;align-items:center;justify-content:center}
.stat{width:250px;text-align:center;color:#fff}
.stat+.stat{border-left:1.5px solid rgba(255,255,255,.7)}
.stat b{display:block;font-family:var(--serif);font-weight:500;font-size:28px}
.stat span{font-size:10px}

/* data centers */
.focus{height:763px}
.focus-photo{position:absolute;left:90px;top:107px;width:440px;height:549px;background:linear-gradient(180deg,#2a2f35 0%,#6d747c 45%,#d8dcdf 60%,#5a6067 80%,#23272c 100%);box-shadow:0 20px 40px rgba(0,0,0,.28)}
.eyebrow{font-size:13px;color:var(--blue)}
.focus .eyebrow{position:absolute;left:640px;top:176px}
.focus h2{position:absolute;left:640px;top:220px;font-family:var(--serif);font-weight:500;font-size:40px;line-height:1.1}
.focus .lead{position:absolute;left:640px;top:336px;width:425px;font-size:15px;line-height:1.6;color:var(--muted)}
.feature{position:absolute;left:640px;display:flex;gap:12px;font-size:13px;color:var(--muted)}
.feature svg{width:16px;height:16px;flex:none}
.feature b{display:block;color:var(--ink);font-weight:600;margin-bottom:3px}
.focus .btn{position:absolute;left:640px;top:613px;width:159px;height:45px;background:var(--green)}

/* competences */
.skills{height:638px;background:var(--sky)}
.skills .eyebrow{position:absolute;top:78px;width:100%;text-align:center;color:var(--green)}
.skills h2{position:absolute;top:108px;width:100%;text-align:center;font-family:var(--serif);font-weight:500;font-size:42px}
.card{position:absolute;top:205px;width:302px;height:284px;background:#fff;border:1px solid #d6e4ec;padding:34px 34px}
.card svg{width:24px;height:24px}
.card h3{font-family:var(--serif);font-weight:600;font-size:21px;margin:26px 0 14px}
.card p{font-size:13px;line-height:1.55;color:var(--muted)}
.card a{position:absolute;left:34px;bottom:36px;font-size:13px;color:var(--green);text-decoration:none}
.skills .btn{position:absolute;left:514px;top:522px;width:167px;height:44px;background:var(--blue)}

/* risk check */
.risk{height:714px;overflow:hidden}
.risk-photo{position:absolute;inset:0;background:linear-gradient(120deg,#1a6ea8 0%,#2783bf 50%,#1f79b4 100%)}
.risk h2{position:absolute;left:122px;top:218px;font-family:var(--serif);font-weight:500;font-size:40px;color:#fff}
.risk .lead{position:absolute;left:122px;top:295px;width:445px;font-size:15px;line-height:1.6;color:#eef5fa}
.steps{position:absolute;left:122px;top:390px;list-style:none;color:#fff;font-size:13px}
.steps li{display:flex;align-items:center;gap:14px;height:26px;margin-bottom:14px}
.steps span{width:26px;height:26px;background:var(--green);display:flex;align-items:center;justify-content:center;font-size:12px}
.form{position:absolute;left:614px;top:81px;width:469px;height:552px;background:#fff;padding:44px 41px}
.form h3{font-family:var(--serif);font-weight:600;font-size:22px;margin-bottom:22px}
.field{margin-bottom:18px}
.field label{display:block;font-size:10px;letter-spacing:.14em;font-weight:600;color:#333;margin-bottom:6px}
.field div{border-bottom:1px solid #c9ced3;font-size:13px;color:#6a7178;padding:8px 10px 10px;display:flex;justify-content:space-between}
.field .area{height:68px}
.consent{display:flex;gap:10px;font-size:9.5px;color:#555;line-height:1.35;margin:24px 0 14px}
.consent i{width:13px;height:13px;border:1px solid #aaa;flex:none;margin-top:2px}
.consent u{color:#333}
.submit{background:var(--green);color:#fff;font-size:11px;letter-spacing:.14em;font-weight:600;height:36px;display:flex;align-items:center;justify-content:center}

/* cta + footer */
.closing{height:1043px;overflow:hidden}
.closing-dark{position:absolute;left:0;right:0;top:342px;bottom:0;background:linear-gradient(180deg,#0b4a73 0%,#0e3a5a 45%,#123550 100%)}
.cta{position:absolute;left:128px;top:134px;width:944px;height:322px;border-radius:24px;background:linear-gradient(120deg,#9acb4c 0%,#8cbf3f 55%,#82b637 100%);text-align:center;color:#fff}
.cta h2{font-family:var(--serif);font-weight:500;font-size:40px;margin-top:60px}
.cta p{width:460px;margin:24px auto 0;font-size:14px;line-height:1.5}
.cta .btn{position:absolute;left:315px;top:207px;width:314px;height:59px;background:var(--blue);font-size:13px;letter-spacing:.14em}
.foot{position:absolute;top:592px;left:120px;right:120px;display:grid;grid-template-columns:247px 247px 247px 1fr;color:#fff;font-size:13px}
.foot .brand{font-size:30px}
.foot .about{margin-top:28px;line-height:1.55;width:215px}
.foot h4{font-weight:400;font-size:13px;color:var(--green);margin-bottom:26px}
.foot ul{list-style:none}
.foot li{margin-bottom:20px}
.rule{position:absolute;left:82px;right:82px;top:805px;border-top:1px solid rgba(255,255,255,.25)}
.copy{position:absolute;top:866px;width:100%;text-align:center;color:#fff;font-size:13px}
</style>
</head>
<body>

<header class="hero">
  <div class="hero-photo" role="img" aria-label="Glasfassaden von Hochhäusern aus der Froschperspektive, blau getönt"></div>
  <nav class="nav">
    <div class="brand">Veltrana<i></i></div>
    <div class="nav-links">
      <a class="active">BAUFINANZIERUNG</a><a>VERSICHERUNGEN</a><a>KAPITALANLAGE</a><a>KONTAKT</a>
    </div>
    <a class="nav-cta">TERMIN VEREINBAREN</a>
  </nav>
  <h1>Maßgeschneiderte<br>Finanzierung für<br>Gewerbe &amp; Industrie.</h1>
  <p>Wir strukturieren komplexe Finanzierungen für Immobilien, Rechenzentren und Unternehmenswachstum. Unabhängig, diskret und mit exzellentem Marktzugang.</p>
  <a class="btn btn-primary">Anfrage stellen <svg viewBox="0 0 12 12"><path d="M1 6h9M6 2l4 4-4 4" stroke="#fff" stroke-width="1.6" fill="none"/></svg></a>
  <a class="btn btn-ghost">Unsere Expertise</a>
</header>

<section class="stats">
  <div class="stat"><b>&gt; 15</b><span>Jahre Erfahrung</span></div>
  <div class="stat"><b>€ 2,5 Mrd.</b><span>Begleitetes Volumen</span></div>
  <div class="stat"><b>120+</b><span>Erfolgreiche Projekte</span></div>
  <div class="stat"><b>100%</b><span>Unabhängigkeit</span></div>
</section>

<section class="focus">
  <div class="focus-photo" role="img" aria-label="Gang in einem Rechenzentrum mit Serverschränken"></div>
  <div class="eyebrow">Branchenfokus</div>
  <h2>Digitale Infrastruktur &amp;<br>Data Centers</h2>
  <p class="lead">Wir verstehen die Komplexität großskaliger Technologieprojekte. Unsere Spezialisierung umfasst die strukturierte Finanzierung von Rechenzentren und digitaler Infrastruktur mit Fokus auf langfristiges Risikomanagement und ESG-konforme Kapitalbeschaffung.</p>
  <div class="feature" style="top:493px"><svg viewBox="0 0 16 16"><path d="M1 5L8 1l7 4zM3 6v6M6.3 6v6M9.7 6v6M13 6v6M1 14h14" stroke="#8cbf3f" stroke-width="1.4" fill="none"/></svg><div><b>Projektfinanzierung</b>Asset-basierte Strukturen für komplexe Bauvorhaben.</div></div>
  <div class="feature" style="top:546px"><svg viewBox="0 0 16 16"><path d="M2 14V10M6 14V8M10 14V9M14 14V5M1 7l5-4 4 3 5-4" stroke="#8cbf3f" stroke-width="1.4" fill="none"/></svg><div><b>Risikomanagement</b>Präzise Modellierung von Marktentwicklungen und Zinsrisiken.</div></div>
  <a class="btn">Anfrage stellen <svg viewBox="0 0 12 12"><path d="M1 6h9M6 2l4 4-4 4" stroke="#fff" stroke-width="1.6" fill="none"/></svg></a>
</section>

<section class="skills">
  <div class="eyebrow">Expertise</div>
  <h2>Kernkompetenzen</h2>
  <div class="card" style="left:118px">
    <svg viewBox="0 0 24 24"><path d="M3 21V4h11v17M14 9h7v12M1 21h22M6 7h2M10 7h1M6 11h2M10 11h1M6 15h2M10 15h1M17 13h1M17 17h1" stroke="#8cbf3f" stroke-width="1.6" fill="none"/></svg>
    <h3>Baufinanzierung</h3>
    <p>Strategische Finanzierungslösungen für Wohn-, Gewerbe- und Spezialimmobilien mit Fokus auf optimierte Kapitalstrukturen.</p>
    <a>Mehr erfahren &nbsp;›</a>
  </div>
  <div class="card" style="left:446px">
    <svg viewBox="0 0 24 24"><path d="M12 2l8 3v6c0 5-3.5 9-8 11-4.5-2-8-6-8-11V5z" stroke="#8cbf3f" stroke-width="1.6" fill="none"/><path d="M8.5 12l2.5 2.5 4.5-5" stroke="#8cbf3f" stroke-width="1.6" fill="none"/></svg>
    <h3>Versicherungen</h3>
    <p>Ganzheitliche Risikoanalyse und Absicherung für Unternehmen, Industrieobjekte und anspruchsvolle Privatmandanten.</p>
    <a>Mehr erfahren &nbsp;›</a>
  </div>
  <div class="card" style="left:776px">
    <svg viewBox="0 0 24 24"><rect x="4" y="4" width="18" height="12" stroke="#8cbf3f" stroke-width="1.6" fill="none"/><circle cx="13" cy="10" r="2.6" stroke="#8cbf3f" stroke-width="1.6" fill="none"/><path d="M2 7v12h17" stroke="#8cbf3f" stroke-width="1.6" fill="none"/></svg>
    <h3>Kapitalanlage</h3>
    <p>Exklusive Anlagestrategien und Zugang zu institutionellen Assetklassen für nachhaltigen Vermögenserhalt.</p>
    <a>Mehr erfahren &nbsp;›</a>
  </div>
  <a class="btn">Anfrage stellen <svg viewBox="0 0 12 12"><path d="M1 6h9M6 2l4 4-4 4" stroke="#fff" stroke-width="1.6" fill="none"/></svg></a>
</section>

<section class="risk">
  <div class="risk-photo" role="img" aria-label="Person prüft Vertragsunterlagen am Schreibtisch, blau getönt"></div>
  <h2>Der Fundaris Risk-Check.</h2>
  <p class="lead">Besitzen Ihre aktuellen Verträge noch Marktrelevanz? In einer kostenfreien Erstprüfung analysieren wir Ihr bestehendes Portfolio auf Deckungslücken und Optimierungspotenziale.</p>
  <ol class="steps">
    <li><span>1</span>Übermittlung Ihrer aktuellen Policen-Übersicht.</li>
    <li><span>2</span>Benchmark-Vergleich mit aktuellen Marktkonditionen.</li>
    <li><span>3</span>Präsentation strategischer Handlungsempfehlungen.</li>
  </ol>
  <div class="form">
    <h3>Analyse anfordern</h3>
    <div class="field"><label>VOLLSTÄNDIGER NAME</label><div>Maximilian Mustermann</div></div>
    <div class="field"><label>E-MAIL ADRESSE</label><div>m.mustermann@unternehmen.de</div></div>
    <div class="field"><label>UNTERNEHMENSBEREICH</label><div style="color:#222">Wählen Sie einen Bereich... <svg width="12" height="12" viewBox="0 0 12 12"><path d="M2 4l4 4 4-4" stroke="#444" stroke-width="1.4" fill="none"/></svg></div></div>
    <div class="field"><label>IHRE NACHRICHT (OPTIONAL)</label><div class="area">Kurze Beschreibung Ihrer Anforderungen...</div></div>
    <div class="consent"><i></i><span>Ich stimme zu, dass meine Daten zur Bearbeitung dieser Anfrage gemäß der <u>Datenschutzerklärung</u> verarbeitet werden.</span></div>
    <div class="submit">ANALYSE JETZT STARTEN</div>
  </div>
</section>

<section class="closing">
  <div class="closing-dark"></div>
  <div class="cta" role="img" aria-label="Grün getönter Schreibtisch mit Laptop und Unterlagen">
    <h2>Bereit für Ihr nächstes Projekt?</h2>
    <p>Lassen Sie uns gemeinsam die optimale Finanzierungsstrategie für Ihr Vorhaben entwickeln. Diskret, kompetent und unabhängig.</p>
    <a class="btn">ERSTBERATUNG VEREINBAREN</a>
  </div>
  <footer class="foot">
    <div><div class="brand">Veltrana<i></i></div><p class="about">Ihr Partner für exzellente Finanzberatung und strukturierte Lösungen im gewerblichen Bereich.</p></div>
    <div><h4>Expertise</h4><ul><li>Baufinanzierung</li><li>Versicherungen</li><li>Kapitalanlage</li></ul></div>
    <div><h4>Unternehmen</h4><ul><li>Über uns</li><li>Karriere</li><li>Compliance</li></ul></div>
    <div><h4>Rechtliches</h4><ul><li>Impressum</li><li>Datenschutz</li><li>AGB</li></ul></div>
  </footer>
  <div class="rule"></div>
  <div class="copy">© 2026 Veltrana. Alle Rechte vorbehalten.</div>
</section>

</body>
</html>
```